Graphic Design Set for Banner Ads - Sizes and Specs for Bidlane

We need a set of 6 ads of the following sizes created for Bidlane:

Medium rectangle: 300×250
Leaderboard: 728×90
Wide skyscraper: 160×600
Large rectangle: 300x600
Mobile leaderboard: 320×50

Here are the Formatting Guidelines (WEB ADS): https://help.bidlane.com/hc/en-us/articles/583920147-Ad-Content-and-Format-Guidelines

Here is the website: https://mavenhollowcare.com/

Here are some words for the ad - feel free to use creative liberties if you have something better or need less words.

1. The Future of Aging is Here

2. Dementia At-Home Care

3. Benefits of an Assisted Living from the Privacy of Your Home - link to

4. Idaho's New Senior Care Option

5. The Security of Senior Living from the Comfort of Your Home

I have the images for all website photos, if you need more images, please let me know.

Target Market(s)

Women age 55+

Industry/Entity Type

Graphic Design

Requirements
Must have
• Incorporate website imagery as much as possible
Should not have
• a feeling of helplessness, old, etc.

```html
<!DOCTYPE html>
<html lang="en">
<head>
<meta charset="utf-8">
<title>Maven Hollow – Skyscraper Ad Set</title>
<link href="https://fonts.googleapis.com/css2?family=Raleway:wght@500;600&display=swap" rel="stylesheet">
<style>
  :root {
    --stage: #383838;
    --ink: #1f1f1f;
    --gold: #c1962f;
    --gold-light: #e6c46a;
    --paper-top: #ffffff;
    --paper-bottom: #dcdcdc;
    --strip: #6a6a6a;
    --button: #1c1c1c;
  }
  * { margin: 0; padding: 0; box-sizing: border-box; }
  html, body { width: 1200px; height: 1200px; overflow: hidden; background: var(--stage); }
  .stage { position: relative; width: 1200px; height: 1200px; }
  .ad-grid {
    position: absolute; left: 345px; top: 95px;
    width: 616px; height: 1100px;
    transform: scale(0.8276); transform-origin: 0 0;
    display: grid; grid-template-columns: 300px 300px; column-gap: 16px; row-gap: 24px;
  }
  .ad {
    position: relative; width: 300px; height: 600px; overflow: hidden;
    background: linear-gradient(180deg, var(--paper-top) 45%, var(--paper-bottom) 100%);
    box-shadow: 0 3px 8px rgba(0,0,0,0.45);
    font-family: "Raleway", sans-serif; text-align: center; color: var(--ink);
  }
  .ad-photo { position: absolute; left: 0; top: 0; width: 300px; height: 290px; }
  .photo-armchair { background: linear-gradient(160deg, #e9dccb 0%, #a88d74 55%, #6b5444 100%); }
  .photo-window   { background: linear-gradient(120deg, #f2efe9 0%, #d8cfc2 45%, #9f8a66 100%); }
  .photo-embrace  { background: linear-gradient(140deg, #d9cfc6 0%, #b8988a 50%, #6e4a3c 100%); }
  .photo-puzzle   { background: linear-gradient(135deg, #e7ecee 0%, #a9b6c6 50%, #7d6a64 100%); }
  .ad-swoosh { position: absolute; left: 0; top: 200px; width: 300px; height: 100px; }
  .ad-headline {
    position: absolute; left: 0; right: 0; top: 300px;
    font-size: 23px; font-weight: 600; line-height: 24px; letter-spacing: -0.2px;
  }
  .ad-offer { position: absolute; left: 0; right: 0; font-size: 13px; line-height: 14px; font-weight: 500; }
  .ad-offer .offer-name { color: var(--ink); }
  .ad-offer .offer-plan { color: var(--gold); font-weight: 600; }
  .offer-assist { top: 384px; }
  .offer-memory { top: 420px; }
  .ad-brand {
    position: absolute; left: 0; right: 0; top: 462px;
    font-size: 26px; font-weight: 500; letter-spacing: 1px; color: var(--ink);
    display: flex; align-items: center; justify-content: center; gap: 8px;
  }
  .brand-dot { width: 12px; height: 12px; border-radius: 50%; background: var(--gold); }
  .ad-button {
    position: absolute; left: 81px; top: 522px; width: 139px; height: 37px;
    background: var(--button); color: #fff; font-size: 15px; font-weight: 600;
    line-height: 37px; letter-spacing: 0.3px;
  }
  .ad-url { position: absolute; left: 0; right: 0; top: 562px; font-size: 15px; color: var(--gold); font-weight: 500; }
  .ad-strip { position: absolute; left: 0; bottom: 0; width: 300px; height: 12px; background: var(--strip); }
</style>
</head>
<body>
<div class="stage">
  <div class="ad-grid">

    <article class="ad">
      <div class="ad-photo photo-armchair" role="img" aria-label="Smiling senior man relaxing in a floral armchair at home"></div>
      <svg class="ad-swoosh" viewBox="0 0 300 100" preserveAspectRatio="none" aria-hidden="true">
        <defs><linearGradient id="g1" x1="0" x2="1"><stop offset="0" stop-color="#e6c46a"/><stop offset="1" stop-color="#b88a22"/></linearGradient></defs>
        <path d="M0 55 Q150 110 300 15 L300 100 L0 100 Z" fill="url(#g1)"/>
        <path d="M0 62 Q150 112 300 26 L300 100 L0 100 Z" fill="#ffffff"/>
      </svg>
      <h2 class="ad-headline">The Security of<br>Senior Living from the<br>Comfort of Your Home</h2>
      <p class="ad-offer offer-assist"><span class="offer-name">AT-HOME ASSISTANCE</span><br><span class="offer-plan">ASSISTANCE MEMBERSHIP</span></p>
      <p class="ad-offer offer-memory"><span class="offer-name">AT-HOME MEMORY CARE</span><br><span class="offer-plan">MEMORY MEMBERSHIP</span></p>
      <div class="ad-brand"><span class="brand-dot"></span>MAVEN HOLLOW</div>
      <div class="ad-button">LEARN MORE</div>
      <p class="ad-url">mavenhollowcare.com</p>
      <div class="ad-strip"></div>
    </article>

    <article class="ad">
      <div class="ad-photo photo-window" role="img" aria-label="Senior woman opening a sunlit window with arms raised"></div>
      <svg class="ad-swoosh" viewBox="0 0 300 100" preserveAspectRatio="none" aria-hidden="true">
        <defs><linearGradient id="g2" x1="0" x2="1"><stop offset="0" stop-color="#e6c46a"/><stop offset="1" stop-color="#b88a22"/></linearGradient></defs>
        <path d="M0 55 Q150 110 300 15 L300 100 L0 100 Z" fill="url(#g2)"/>
        <path d="M0 62 Q150 112 300 26 L300 100 L0 100 Z" fill="#ffffff"/>
      </svg>
      <h2 class="ad-headline">The Security of<br>Senior Living from the<br>Comfort of Your Home</h2>
      <p class="ad-offer offer-assist"><span class="offer-name">AT-HOME ASSISTANCE</span><br><span class="offer-plan">ASSISTANCE MEMBERSHIP</span></p>
      <p class="ad-offer offer-memory"><span class="offer-name">AT-HOME MEMORY CARE</span><br><span class="offer-plan">MEMORY MEMBERSHIP</span></p>
      <div class="ad-brand"><span class="brand-dot"></span>MAVEN HOLLOW</div>
      <div class="ad-button">LEARN MORE</div>
      <p class="ad-url">mavenhollowcare.com</p>
      <div class="ad-strip"></div>
    </article>

    <article class="ad">
      <div class="ad-photo photo-embrace" role="img" aria-label="Senior woman and younger woman touching foreheads and smiling"></div>
      <svg class="ad-swoosh" viewBox="0 0 300 100" preserveAspectRatio="none" aria-hidden="true">
        <defs><linearGradient id="g3" x1="0" x2="1"><stop offset="0" stop-color="#e6c46a"/><stop offset="1" stop-color="#b88a22"/></linearGradient></defs>
        <path d="M0 55 Q150 110 300 15 L300 100 L0 100 Z" fill="url(#g3)"/>
        <path d="M0 62 Q150 112 300 26 L300 100 L0 100 Z" fill="#ffffff"/>
      </svg>
      <h2 class="ad-headline">The Security of<br>Senior Living from the<br>Comfort of Your Home</h2>
      <p class="ad-offer offer-assist"><span class="offer-name">AT-HOME ASSISTANCE</span><br><span class="offer-plan">ASSISTANCE MEMBERSHIP</span></p>
      <p class="ad-offer offer-memory"><span class="offer-name">AT-HOME MEMORY CARE</span><br><span class="offer-plan">MEMORY MEMBERSHIP</span></p>
      <div class="ad-brand"><span class="brand-dot"></span>MAVEN HOLLOW</div>
      <div class="ad-button">LEARN MORE</div>
      <p class="ad-url">mavenhollowcare.com</p>
      <div class="ad-strip"></div>
    </article>

    <article class="ad">
      <div class="ad-photo photo-puzzle" role="img" aria-label="Senior woman and young woman doing a crossword puzzle together"></div>
      <svg class="ad-swoosh" viewBox="0 0 300 100" preserveAspectRatio="none" aria-hidden="true">
        <defs><linearGradient id="g4" x1="0" x2="1"><stop offset="0" stop-color="#e6c46a"/><stop offset="1" stop-color="#b88a22"/></linearGradient></defs>
        <path d="M0 55 Q150 110 300 15 L300 100 L0 100 Z" fill="url(#g4)"/>
        <path d="M0 62 Q150 112 300 26 L300 100 L0 100 Z" fill="#ffffff"/>
      </svg>
      <h2 class="ad-headline">The Security of<br>Senior Living from the<br>Comfort of Your Home</h2>
      <p class="ad-offer offer-assist"><span class="offer-name">AT-HOME ASSISTANCE</span><br><span class="offer-plan">ASSISTANCE MEMBERSHIP</span></p>
      <p class="ad-offer offer-memory"><span class="offer-name">AT-HOME MEMORY CARE</span><br><span class="offer-plan">MEMORY MEMBERSHIP</span></p>
      <div class="ad-brand"><span class="brand-dot"></span>MAVEN HOLLOW</div>
      <div class="ad-button">LEARN MORE</div>
      <p class="ad-url">mavenhollowcare.com</p>
      <div class="ad-strip"></div>
    </article>

  </div>
</div>
</body>
</html>
```